Photography blog homepage design

I need a new webpage design for my photography blog. My blog focuses on post-processing techniques, particularly in luminosity masking, HDR photography and other advanced photo editing skills. I want the new homepage to let visitors know instantly what the blog is about as this is currently not very obvious from the feedback I received. Apart from that, the homepage should also inform/showcase latest blog post and/or popular blog post and/or some of the training courses I offer (that's my idea, but I leave it to your expertise). There should also ideally have a CTA that leads visitors to the "Start Here" page where they can learn more about my blog. The bulk of my audience is intermediate/advanced photographers who are above 30-35 years old, with a significant group in the 60 to >75 age group. The design should convey trust and creativity at the same time. The color theme for my blog is orange and dark grey. URL is www.lumivarnic.com, you can use the current content on that page.

Target Market(s)

Intermediate/advanced photographers (hobbyist or professional) age 35-75 years old.

Number of Pages Required

1 page

Font styles to use
Sans Serif

Colors
faa54b
f68e4e
f78f20

Requirements
Must have
• Upside down homepage (menus at the bottom)

```html
<!DOCTYPE html>
<html lang="en">
<head>
<meta charset="utf-8">
<title>Lumivarnic — Photography Blog</title>
<link href="https://fonts.googleapis.com/css2?family=Kreon:wght@300;400;700&family=Roboto+Condensed:wght@400&display=swap" rel="stylesheet">
<style>
:root{
  --orange:#f78f20;
  --orange-soft:#faa54b;
  --orange-mid:#f68e4e;
  --btn:#f9b27a;
  --ink:#2b2b2b;
  --muted:#777;
  --line:#ddd;
  --dark:#2e2e2e;
  --white:#fff;
}
*{box-sizing:border-box;margin:0;padding:0}
html,body{width:1200px;height:3010px;overflow:hidden;background:var(--white)}
body{position:relative;font-family:"Kreon",serif;color:var(--ink)}
.abs{position:absolute}
a{color:inherit;text-decoration:none}

/* top bar */
.util-links{left:172px;top:9px;font-size:11px;color:#444}
.util-links span{margin:0 5px}
.brand{font-weight:700;color:var(--ink);letter-spacing:1px;display:flex;align-items:center;gap:8px}
.brand .dot{width:30px;height:30px;border-radius:50%;background:var(--orange)}
.brand-top{left:0;width:1200px;top:22px;justify-content:center;font-size:40px;line-height:44px}
.social-top{left:917px;top:9px;display:flex;gap:6px}
.social-top i{display:block;width:16px;height:16px;border-radius:50%;background:var(--orange-mid)}
.login{left:950px;top:56px;width:76px;height:22px;background:var(--btn);font-size:12px;text-align:center;line-height:22px;border-radius:2px}

/* hero */
.hero{left:0;top:84px;width:1200px;height:392px;background:linear-gradient(180deg,#5f5f86 0%,#c58b9e 25%,#7c6a62 55%,#3a3530 80%,#252428 100%)}
.hero-name{left:0;width:1200px;top:224px;text-align:center;font-size:96px;font-weight:700;color:var(--white);letter-spacing:2px}
.hero-arrow{top:267px;width:19px;height:26px;background:var(--white);display:flex;align-items:center;justify-content:center}

/* section titles */
.section-title{left:0;width:1200px;text-align:center;font-size:34px;font-weight:300;color:#333}

/* cards */
.card{top:574px;width:268px;height:428px;border:1px solid #e3e3e3;border-radius:3px;background:var(--white)}
.card.lifted{box-shadow:0 4px 14px rgba(0,0,0,.12);border-color:#eee}
.card-media{height:170px;position:relative}
.card-media svg{position:absolute;left:112px;top:63px}
.card-body{padding:18px 22px}
.card-cat{font-size:13px;color:var(--orange-mid)}
.card-title{font-size:17px;line-height:26px;color:#333;margin-top:8px;font-weight:300}
.card-text{font-size:11.5px;line-height:21px;color:var(--muted);margin-top:10px}
.btn{display:inline-block;background:var(--btn);color:#333;font-size:13px;text-align:center}
.card .btn{width:106px;height:31px;line-height:31px;margin-top:16px}
.big-arrow{top:765px;width:46px;height:47px;background:var(--orange-mid);border-radius:3px;display:flex;align-items:center;justify-content:center}

/* courses */
.course{top:1110px;width:268px;height:270px;border-radius:3px;display:flex;align-items:center;justify-content:center;text-align:center;color:var(--white);font-size:26px;line-height:33px;text-shadow:0 1px 4px rgba(0,0,0,.5)}

/* latest posts */
.latest-title{left:172px;top:1444px;font-size:34px;font-weight:300;color:#333}
.post-media{left:173px;width:614px;height:324px}
.post-title{left:173px;font-size:16px;color:#333;font-weight:400}
.post-meta{left:173px;font-size:11.5px;color:#555}
.post-meta span{margin-left:10px}
.post-text{left:173px;width:560px;font-size:12px;line-height:21px;color:var(--muted)}
.post-btn{left:173px;width:106px;height:31px;line-height:31px}

/* sidebar */
.side-title{left:830px;top:1447px;font-size:21px;color:#333;font-weight:400}
.portrait{left:830px;top:1483px;width:197px;height:226px;background:linear-gradient(180deg,#9a9a9a,#b8b0a7 60%,#8d929a)}
.side-name{left:830px;top:1725px;font-size:13px;color:#333;font-family:"Roboto Condensed",sans-serif}
.side-text{left:831px;top:1752px;width:196px;font-size:11.5px;line-height:16.5px;color:var(--muted)}
.side-rule{left:830px;top:1850px;width:197px;border-top:1px solid var(--line)}
.join{left:830px;top:1875px;width:197px;text-align:center;font-size:13px;line-height:17px;color:#444}
.email{left:830px;top:1923px;width:197px;height:31px;border:1px solid var(--line);font-size:9.5px;font-style:italic;color:#666;padding:9px 14px}
.subscribe{left:830px;top:1964px;width:197px;height:30px;line-height:30px;background:var(--orange-soft);font-size:13px}
.ad{left:830px;top:2046px;width:197px;height:427px;background:var(--dark);color:var(--white);text-align:center;display:flex;flex-direction:column;justify-content:center}
.ad strong{font-size:34px;line-height:39px;font-weight:400}
.ad span{font-size:19px;margin-top:14px}

/* pagination */
.pager{left:173px;top:2640px;display:flex;border:1px solid var(--line);font-size:10px;color:#555;height:20px}
.pager span{padding:0 10px;line-height:18px;border-right:1px solid var(--line)}
.pager span:last-child{border-right:0}
.pager .current{background:#666;color:var(--white)}

/* footer */
.contact-btn{left:493px;top:2706px;width:214px;height:64px;line-height:64px;background:var(--btn);font-size:26px}
.brand-foot{left:0;width:1200px;top:2800px;justify-content:center;font-size:40px;line-height:44px}
.social-foot{left:514px;top:2876px;display:flex;gap:11px}
.social-foot i{display:block;width:26px;height:26px;border-radius:50%;background:var(--orange-mid)}
.foot-rule{left:318px;top:2927px;width:564px;border-top:1px solid var(--line)}
.copyright{left:0;width:1200px;top:2938px;text-align:center;font-size:10.5px;color:#555}

/* bottom navigation */
.navbar{left:0;top:2964px;width:1200px;height:46px;background:linear-gradient(180deg,#fbae6a,#f79a48)}
.nav-links{left:173px;top:2979px;display:flex;gap:20px;font-size:13px;color:#222;font-family:"Roboto Condensed",sans-serif}
.nav-links .active{border-bottom:3px solid #222;padding-bottom:2px}
.search{left:808px;top:2973px;width:218px;height:28px;background:var(--white);border-radius:2px;font-size:11px;color:#aaa;padding:7px 16px}
.search svg{position:absolute;right:8px;top:8px}
</style>
</head>
<body>

<header>
  <div class="abs util-links"><a href="#">Privacy Policy</a><span>|</span><a href="#">Contact</a></div>
  <div class="abs brand brand-top"><i class="dot"></i>LUMIVARNIC</div>
  <div class="abs social-top"><i></i><i></i><i></i><i></i><i></i></div>
  <a class="abs login" href="#">Login</a>
</header>

<section class="hero-block">
  <div class="abs hero" role="img" aria-label="Photo of a domed capitol building at sunset with reflections on wet pavement"></div>
  <div class="abs hero-name">LUMIVARNIC</div>
  <div class="abs hero-arrow" style="left:23px"><svg width="8" height="10"><path d="M6 1 L2 5 L6 9" fill="none" stroke="#222" stroke-width="2"/></svg></div>
  <div class="abs hero-arrow" style="left:1157px"><svg width="8" height="10"><path d="M2 1 L6 5 L2 9" fill="none" stroke="#222" stroke-width="2"/></svg></div>
</section>

<section class="popular">
  <h2 class="abs section-title" style="top:510px">Popular Posts</h2>
  <div class="abs big-arrow" style="left:68px"><svg width="14" height="20"><path d="M11 2 L3 10 L11 18" fill="none" stroke="#222" stroke-width="3"/></svg></div>
  <div class="abs big-arrow" style="left:1078px"><svg width="14" height="20"><path d="M3 2 L11 10 L3 18" fill="none" stroke="#222" stroke-width="3"/></svg></div>

  <article class="abs card" style="left:173px">
    <div class="card-media" role="img" aria-label="Video still of red sandstone rock formations under a blue sky" style="background:linear-gradient(160deg,#7a3f25,#3d7ea8 50%,#b4612f)">
      <svg width="44" height="44"><circle cx="22" cy="22" r="20" fill="#222" stroke="#fff" stroke-width="2"/><path d="M17 13 L31 22 L17 31Z" fill="#fff"/></svg>
    </div>
    <div class="card-body">
      <div class="card-cat">HDR photography</div>
      <h3 class="card-title">I am a blogger living in New York. This is my blog,</h3>
      <p class="card-text">Lorem Ipsum is simply dummy text of the printing and typesetting industry. Lorem Ipsum has been the industry's standard dummy text ever since the 1500s.</p>
      <a class="btn" href="#">Read More</a>
    </div>
  </article>

  <article class="abs card lifted" style="left:465px">
    <div class="card-media" role="img" aria-label="Video still of snowy mountain peaks reflected in a lake" style="background:linear-gradient(180deg,#8d97b5,#c9c6cf 35%,#3b4f6e 65%,#1f2c45)">
      <svg width="44" height="44"><circle cx="22" cy="22" r="20" fill="#222" stroke="#fff" stroke-width="2"/><path d="M17 13 L31 22 L17 31Z" fill="#fff"/></svg>
    </div>
    <div class="card-body">
      <div class="card-cat">Post-Processing Techniques</div>
      <h3 class="card-title">I am a blogger living in New York. This is my blog,</h3>
      <p class="card-text">Lorem Ipsum is simply dummy text of the printing and typesetting industry. Lorem Ipsum has been the industry's standard dummy text ever since the 1500s.</p>
      <a class="btn" href="#">Read More</a>
    </div>
  </article>

  <article class="abs card" style="left:757px">
    <div class="card-media" role="img" aria-label="Video still of old pier posts in calm water at sunset" style="background:linear-gradient(180deg,#3b4a7a,#c58a6e 40%,#6b5a4d 65%,#2c3555)">
      <svg width="44" height="44"><circle cx="22" cy="22" r="20" fill="#222" stroke="#fff" stroke-width="2"/><path d="M17 13 L31 22 L17 31Z" fill="#fff"/></svg>
    </div>
    <div class="card-body">
      <div class="card-cat">Particularly in Luminosity Masking</div>
      <h3 class="card-title">I am a blogger living in New York. This is my blog,</h3>
      <p class="card-text">Lorem Ipsum is simply dummy text of the printing and typesetting industry. Lorem Ipsum has been the industry's standard dummy text ever since the 1500s.</p>
      <a class="btn" href="#">Read More</a>
    </div>
  </article>
</section>

<section class="courses">
  <h2 class="abs section-title" style="top:1050px">Courses</h2>
  <a class="abs course" href="#" style="left:173px;background:linear-gradient(135deg,#6a5a48,#e0b772 45%,#1c1712 75%)" role="img" aria-label="Silhouette of a photographer with a camera against a golden sky">HDR photography</a>
  <a class="abs course" href="#" style="left:465px;background:linear-gradient(180deg,#3a3a3a,#8a8a8a 40%,#555 70%,#2a2a2a)" role="img" aria-label="Black and white field scene with a woman holding a coloured watering can">Post- Processing<br>Techniques</a>
  <a class="abs course" href="#" style="left:757px;background:linear-gradient(180deg,#b69a98,#d08c6e 35%,#8a6a8e 60%,#5a4660)" role="img" aria-label="Lavender field at sunset shown before and after editing">Particularly in<br>Luminosity Masking</a>
</section>

<main>
  <h2 class="abs latest-title">Latest Posts</h2>

  <div class="abs post-media" style="top:1498px;background:linear-gradient(170deg,#9aa6b5,#5f7385 30%,#2f4c60 55%,#a06a3a 75%,#4a3a2c)" role="img" aria-label="Fjord between snow-dusted mountains at golden hour"></div>
  <h3 class="abs post-title" style="top:1844px">YOur Blog Title Here.</h3>
  <div class="abs post-meta" style="top:1873px">Jan 11, 2019<span>Lorem Ipsum, Lifestyle</span></div>
  <p class="abs post-text" style="top:1899px">Lorem Ipsum is simply dummy text of the printing and typesetting industry. Lorem Ipsum has been the industry's standard dummy text ever since the 1500s., when an unknown printer took a galley of type and scrambled it to make a type specimen book. It has survived not only five centuries, but also the leap into electronic typesetting, remaining essentially unchanged.</p>
  <a class="abs btn post-btn" href="#" style="top:1995px">Read More</a>

  <div class="abs post-media" style="top:2068px;background:linear-gradient(170deg,#2d3a52,#4a5a78 35%,#2a3a4c 60%,#5f7f99 80%,#3a4a5a)" role="img" aria-label="Dark mountains above a beach with rolling waves"></div>
  <h3 class="abs post-title" style="top:2414px">YOur Blog Title Here.</h3>
  <div class="abs post-meta" style="top:2443px">Jan 11, 2019<span>Lorem Ipsum, Lifestyle</span></div>
  <p class="abs post-text" style="top:2469px">Lorem Ipsum is simply dummy text of the printing and typesetting industry. Lorem Ipsum has been the industry's standard dummy text ever since the 1500s., when an unknown printer took a galley of type and scrambled it to make a type specimen book. It has survived not only five centuries, but also the leap into electronic typesetting, remaining essentially unchanged.</p>
  <a class="abs btn post-btn" href="#" style="top:2565px">Read More</a>

  <div class="abs pager"><span>« Previous</span><span>1</span><span class="current">2</span><span>3</span><span>4</span><span>&nbsp;&nbsp;&nbsp;</span><span>6</span><span>Next »</span></div>
</main>

<aside>
  <h3 class="abs side-title">About Me</h3>
  <div class="abs portrait" role="img" aria-label="Portrait photo of the blog author"></div>
  <div class="abs side-name">Hi....I am Marlo Venn</div>
  <p class="abs side-text">Neque porro quisquam est qui dolorem ipsum quia dolor sit amet, consectetur, adipisci velit. Neque porro quisquam est qui dolorem ipsum quia dolor sit amet,</p>
  <div class="abs side-rule"></div>
  <p class="abs join">Join for free to have posts<br>delivered to your inbox.</p>
  <div class="abs email">Enter your email address</div>
  <a class="abs btn subscribe" href="#">Subscribe Now</a>
  <div class="abs ad"><strong>Your Ad<br>Here</strong><span>270 x 570</span></div>
</aside>

<footer>
  <a class="abs btn contact-btn" href="#">Contact Me</a>
  <div class="abs brand brand-foot"><i class="dot"></i>LUMIVARNIC</div>
  <div class="abs social-foot"><i></i><i></i><i></i><i></i><i></i></div>
  <div class="abs foot-rule"></div>
  <div class="abs copyright">© Lumivarnic 2019, All Right Reserved</div>
</footer>

<nav>
  <div class="abs navbar"></div>
  <div class="abs nav-links"><a class="active" href="#">HOME</a><a href="#">ABOUT</a><a href="#">COURSES</a><a href="#">VIDEOS</a><a href="#">BLOGS</a><a href="#">CONTACT</a></div>
  <div class="abs search">Search
    <svg width="12" height="12" viewBox="0 0 12 12"><circle cx="5" cy="5" r="3.5" fill="none" stroke="#222" stroke-width="1.6"/><line x1="7.6" y1="7.6" x2="11" y2="11" stroke="#222" stroke-width="1.8"/></svg>
  </div>
</nav>

</body>
</html>
```